Zielgruppe
Ich bin freischaffende Autorin und ich suche ein Buchcover (Soft, Hard, Lesmo) für mein erstes Buch. Es handelt sich um einen Thriller, der sich vor allem an Frauen ab 25 und 65 richtet.
Aufgabenstellung
Titel: Die stille Treppe
Autorin: Lena Farukova
Genre: Soft Thriller
Fomate:
- Lesmo
- 12,85 cm x 19,84 cm (5,06' x 7,81“) Softcover
- 13,97 cm x 21,59 cm (5,5' x 8,5') Hardcover
- Blick nach oben in einen Raum hinein
- im Hintergrund ist die gegenüberliegende Ecke sichtbar
- an der Decke hängt eine einzelne rote Glühbirne an einer Leitung
- die rote Glühbirne erleuchte das Zimmer in ein tiefes Blutrot
Das Design darf nicht zu überladen sein.

```html
<!DOCTYPE html>
<html lang="de">
<head>
<meta charset="utf-8">
<title>Die stille Treppe – Buchcover</title>
<link rel="stylesheet" href="https://fonts.googleapis.com/css2?family=Playfair+Display:wght@700;900&family=Montserrat:wght@500&display=swap">
<style>
  :root {
    --backdrop: #c9c9c6;
    --ceiling-top: #e4683f;
    --ceiling-edge: #8e1a1e;
    --wall-red: #d81c22;
    --wall-deep: #5e1214;
    --base-dark: #240404;
    --glow: #ff8a6a;
    --title-dark: #4e0c0f;
    --title-light: #ffffff;
    --label-light: #f4e6e4;
  }
  * { margin: 0; padding: 0; box-sizing: border-box; }
  html, body {
    width: 1166px;
    height: 1200px;
    overflow: hidden;
    background: var(--backdrop);
  }
  .canvas {
    position: relative;
    width: 1166px;
    height: 1200px;
  }
  .book-cover {
    position: absolute;
    left: 246px;
    top: 104px;
    width: 669px;
    height: 992px;
    display: block;
  }
  .title-serif {
    font-family: "Playfair Display", "Didot", serif;
    font-weight: 900;
  }
  .title-small { fill: var(--title-light); font-size: 80px; font-weight: 700; }
  .title-accent { fill: var(--title-dark); font-size: 168px; }
  .title-main { fill: var(--title-light); font-size: 150px; }
  .genre-label {
    font-family: "Montserrat", "Helvetica Neue", sans-serif;
    font-weight: 500;
    font-size: 16px;
    letter-spacing: 5px;
    fill: var(--label-light);
  }
  .author-name {
    font-family: "Montserrat", "Helvetica Neue", sans-serif;
    font-weight: 500;
    font-size: 33px;
    letter-spacing: 7px;
    fill: var(--title-light);
  }
</style>
</head>
<body>
<main class="canvas">
  <svg class="book-cover" viewBox="0 0 669 992" xmlns="http://www.w3.org/2000/svg">
    <defs>
      <linearGradient id="room-shade" x1="0" y1="0" x2="0" y2="1">
        <stop offset="0" stop-color="var(--ceiling-top)"/>
        <stop offset="0.22" stop-color="#d24a34"/>
        <stop offset="0.30" stop-color="var(--ceiling-edge)"/>
        <stop offset="0.31" stop-color="#b52026"/>
        <stop offset="0.52" stop-color="var(--wall-red)"/>
        <stop offset="0.72" stop-color="var(--wall-deep)"/>
        <stop offset="1" stop-color="var(--base-dark)"/>
      </linearGradient>
      <radialGradient id="bulb-glow" cx="341" cy="480" r="320" gradientUnits="userSpaceOnUse">
        <stop offset="0" stop-color="var(--glow)" stop-opacity="0.75"/>
        <stop offset="0.18" stop-color="var(--wall-red)" stop-opacity="0.35"/>
        <stop offset="1" stop-color="var(--wall-red)" stop-opacity="0"/>
      </radialGradient>
    </defs>

    <g class="cover-photo" role="img" aria-label="Fotografie: Blick nach oben in einen rot erleuchteten Raum, an der Decke hängt eine einzelne leuchtende Glühbirne an einer Leitung">
      <rect width="669" height="992" fill="url(#room-shade)"/>
      <rect width="669" height="992" fill="url(#bulb-glow)"/>
    </g>

    <g class="cover-title title-serif">
      <text class="title-small" x="88" y="611">die</text>
      <text class="title-accent" x="604" y="649" text-anchor="end">stille</text>
      <text class="title-main" x="341" y="744" text-anchor="middle">treppe</text>
    </g>

    <text class="genre-label" x="343" y="814" text-anchor="middle">THRILLER</text>
    <text class="author-name" x="344" y="912" text-anchor="middle">LENA FARUKOVA</text>
  </svg>
</main>
</body>
</html>
```